Construction company yard sign

I would like a design for yard signs for my construction company. It will be used to put outside clients homes as we are working for them and will be used as advertisement for neighbors that are passing by the home.

The sign will be 18x24 and a plastic type material.

Target Market(s)

Homeowners

Font styles to use
Sans Serif

Requirements
Must have
• The most important thing about the sign is the visibility of the lettering and phone number 480-913-2647. The next would be Free roof Inspections. and then I would like to have these 3 words on there as well: Flat - Shingle - Tile

```html
<!DOCTYPE html>
<html lang="en">
<head>
<meta charset="utf-8">
<title>Harlow Construction Group – Yard Sign</title>
<link href="https://fonts.googleapis.com/css2?family=Montserrat:wght@800&family=Oswald:wght@500;600&display=swap" rel="stylesheet">
<style>
  :root {
    --brand-blue: #35a6d9;
    --brand-red: #e81f2a;
    --text-grey: #3d3d3f;
    --sign-white: #ffffff;
    --page-bg: #eceeef;
  }
  html, body {
    margin: 0;
    padding: 0;
    width: 1200px;
    height: 1200px;
    overflow: hidden;
    background: var(--page-bg);
  }
  .yard-sign {
    position: absolute;
    left: 40px;
    top: 213px;
    width: 1120px;
    height: 773px;
    background: var(--sign-white);
    overflow: hidden;
    box-shadow: 0 6px 24px rgba(0,0,0,0.12);
  }
  .brand {
    position: absolute;
    left: 43px;
    top: 82px;
    display: flex;
    align-items: center;
    gap: 24px;
  }
  .brand-square {
    width: 92px;
    height: 92px;
    background: var(--brand-red);
  }
  .brand-name {
    font-family: 'Oswald', sans-serif;
    font-weight: 600;
    font-size: 58px;
    line-height: 1;
    letter-spacing: 2px;
    color: var(--brand-blue);
    text-transform: uppercase;
    white-space: nowrap;
  }
  .headline-free {
    position: absolute;
    left: 36px;
    top: 262px;
    margin: 0;
    font-family: 'Montserrat', sans-serif;
    font-weight: 800;
    font-size: 150px;
    line-height: 1;
    letter-spacing: 4px;
    color: var(--brand-red);
  }
  .headline-service {
    position: absolute;
    left: 38px;
    top: 394px;
    margin: 0;
    font-family: 'Oswald', sans-serif;
    font-weight: 600;
    font-size: 80px;
    line-height: 1;
    color: var(--text-grey);
    text-transform: uppercase;
    white-space: nowrap;
  }
  .roof-types {
    position: absolute;
    left: 0;
    top: 500px;
    width: 684px;
    height: 114px;
    background: var(--brand-blue);
    display: flex;
    align-items: center;
    padding-left: 38px;
    box-sizing: border-box;
    font-family: 'Oswald', sans-serif;
    font-weight: 500;
    font-size: 70px;
    color: var(--sign-white);
    text-transform: uppercase;
    white-space: nowrap;
  }
  .roof-types .sep {
    margin: 0 22px;
  }
  .phone-bar {
    position: absolute;
    left: 0;
    top: 617px;
    width: 684px;
    height: 156px;
    background: var(--brand-red);
    display: flex;
    align-items: center;
    padding-left: 36px;
    box-sizing: border-box;
    gap: 26px;
  }
  .phone-icon {
    width: 78px;
    height: 78px;
    flex: none;
  }
  .phone-number {
    font-family: 'Oswald', sans-serif;
    font-weight: 600;
    font-size: 88px;
    line-height: 1;
    color: var(--sign-white);
    white-space: nowrap;
  }
  .brand-decoration {
    position: absolute;
    left: 684px;
    top: 265px;
    width: 436px;
    height: 508px;
    background: linear-gradient(100deg, var(--brand-blue) 0%, var(--brand-blue) 35%, var(--brand-red) 65%, var(--brand-red) 100%);
  }
</style>
</head>
<body>
  <main class="yard-sign">
    <header class="brand">
      <div class="brand-square" aria-hidden="true"></div>
      <span class="brand-name">Harlow Construction Group</span>
    </header>

    <h1 class="headline-free">FREE</h1>
    <h2 class="headline-service">Roof Inspections</h2>

    <div class="roof-types">
      <span>Flat</span><span class="sep">·</span><span>Shingle</span><span class="sep">·</span><span>Tile</span>
    </div>

    <div class="phone-bar">
      <svg class="phone-icon" viewBox="0 0 80 80" aria-hidden="true">
        <circle cx="40" cy="40" r="36" fill="var(--sign-white)" stroke="var(--brand-red)" stroke-width="4"/>
        <circle cx="40" cy="40" r="29" fill="none" stroke="var(--brand-red)" stroke-width="2"/>
        <path d="M28 24c2-2 5-2 6 0l4 7c1 2 0 4-1 5l-2 2c2 5 6 9 11 11l2-2c1-1 3-2 5-1l7 4c2 1 2 4 0 6l-3 3c-3 3-9 2-17-4-8-6-14-14-15-20-1-4 0-7 3-9z" fill="var(--brand-blue)"/>
      </svg>
      <span class="phone-number">480-913-2647</span>
    </div>

    <div class="brand-decoration" role="img" aria-label="Large blue and red house-outline brand graphic"></div>
  </main>
</body>
</html>
```